New Year Resolution Infographic

We are a weight loss company that provides holistic, natural nutrition programs to consumers -- you can see our Web site at www.SlimBirch.com We need a simple infographic to be shared on social media and via email for New Year's day. The topic for the infographic is "how to set and keep your weight loss resolution". We've outlined 5 process steps for consumers to follow to assist with their weight loss resolutions, and we would like to depict this graphically.

Target Market(s)

Women age 35-65 who are planning to make a resolution to lose weight in the new year.

Industry/Entity Type

Health And Wellness

Font styles to use
Sans Serif

Colors
0392cd
9bcb3c

Requirements
Must have
• Initial graphic showing failure stats (see copy)
• Graphic showing process steps in making/keeping a resolution (see copy)
• SlimBirch Logo

```html
<!DOCTYPE html>
<html lang="en">
<head>
<meta charset="utf-8">
<title>How to Set and Reach Your Weight Loss Resolution – SlimBirch</title>
<link rel="stylesheet" href="https://fonts.googleapis.com/css2?family=Roboto+Condensed:wght@300;400;700&display=swap">
<style>
  :root {
    --navy: #12344f;
    --blue: #0392cd;
    --green: #9bcb3c;
    --panel: #e3ebf0;
    --panel-edge: #cfd9df;
    --page: #ffffff;
    --tile: #ffffff;
    --bar: #eceff1;
    --line: #9aa7b0;
  }
  * { margin: 0; padding: 0; box-sizing: border-box; }
  html, body { width: 1200px; height: 2709px; overflow: hidden; background: var(--page); }
  body { font-family: "Roboto Condensed", Arial, sans-serif; position: relative; }

  .sheet {
    position: absolute; left: 63px; top: 108px; width: 1063px; height: 2530px;
    background: var(--panel); border: 2px solid var(--panel-edge);
  }

  .hero {
    position: absolute; left: 141px; top: 146px; width: 900px; height: 320px;
    background: linear-gradient(180deg, #3c4d5c 0%, #7d8c98 45%, #5d6a75 70%, #151b21 100%);
    display: flex; flex-direction: column; align-items: center; justify-content: center;
    color: #fff; text-align: center;
  }
  .hero-title { font-size: 31px; font-weight: 700; text-shadow: 0 2px 4px rgba(0,0,0,.6); }
  .hero-rule { width: 400px; height: 2px; background: rgba(255,255,255,.8); margin: 10px 0 6px; }
  .hero-sub { font-size: 20px; font-weight: 700; }

  .stat {
    position: absolute; top: 503px; height: 410px; background: var(--tile);
    text-align: center; color: var(--navy); font-weight: 700;
  }
  .stat-rank { left: 170px; width: 323px; }
  .stat-rank .lead { font-size: 33px; margin-top: 26px; }
  .stat-rank .big { font-size: 150px; color: var(--green); line-height: 1; margin-top: 30px; letter-spacing: -4px; }
  .stat-rank .tail { font-size: 28px; line-height: 1.25; margin-top: 40px; }
  .stat-keep { left: 678px; width: 334px; }
  .stat-keep .lead { font-size: 33px; margin-top: 18px; }
  .stat-keep svg { display: block; margin: 14px auto 0; }
  .stat-keep .tail { font-size: 32px; line-height: 1.2; margin-top: 8px; }

  .count-badge {
    position: absolute; left: 515px; top: 935px; width: 170px; height: 170px;
    border-radius: 50%; background: #fff; border: 5px solid var(--navy);
    display: flex; align-items: center; justify-content: center;
    font-size: 68px; font-weight: 700; color: var(--navy); z-index: 2;
  }
  .steps-band {
    position: absolute; left: 121px; top: 1066px; width: 929px; height: 158px;
    background: var(--green); color: #fff; text-align: center;
    font-size: 31px; font-weight: 700; line-height: 1.3;
    display: flex; align-items: flex-end; justify-content: center; padding-bottom: 26px;
    text-transform: uppercase;
  }

  .rail { position: absolute; width: 3px; background: var(--line); top: 1300px; height: 830px; }
  .rail-left { left: 200px; }
  .rail-right { left: 294px; }

  .step { position: absolute; left: 190px; width: 820px; height: 114px; }
  .step-num {
    position: absolute; left: 23px; top: -44px; width: 46px; height: 46px; border-radius: 50%;
    background: #fff; border: 3px solid var(--navy); color: var(--navy);
    font-size: 28px; font-weight: 700; display: flex; align-items: center; justify-content: center; z-index: 2;
  }
  .step-icon {
    position: absolute; left: 0; top: 0; width: 117px; height: 114px; background: var(--blue);
    display: flex; align-items: center; justify-content: center;
  }
  .step-bar {
    position: absolute; left: 117px; top: 0; width: 700px; height: 114px; background: var(--bar);
  }
  .step-name {
    position: absolute; left: 152px; top: 22px; font-size: 54px; font-weight: 700;
    color: var(--navy); letter-spacing: -1px; line-height: 1;
  }
  .step-text {
    position: absolute; left: 336px; top: 6px; width: 482px;
    font-size: 18.5px; font-weight: 700; color: var(--blue); line-height: 1.25;
  }

  .foot-rule { position: absolute; left: 134px; top: 2156px; width: 927px; height: 10px; background: var(--green); }
  .site-url {
    position: absolute; left: 0; width: 1200px; top: 2300px; text-align: center;
    font-size: 46px; font-weight: 400; color: var(--blue);
  }
  .brand-box {
    position: absolute; left: 186px; top: 2414px; width: 835px; height: 175px; background: #fff;
    display: flex; align-items: center; justify-content: center; gap: 22px;
  }
  .brand-dot { width: 60px; height: 60px; border-radius: 50%; background: var(--green); }
  .brand-name { font-size: 70px; font-weight: 700; color: var(--green); }
</style>
</head>
<body>
  <div class="sheet"></div>

  <header class="hero" role="img" aria-label="Photo of a runner silhouetted against a cloudy sky">
    <h1 class="hero-title">How to Set and Reach Your Weight Loss Resolution</h1>
    <div class="hero-rule"></div>
    <p class="hero-sub">in 5 simple steps</p>
  </header>

  <section class="stat stat-rank">
    <p class="lead">Weight loss is the</p>
    <p class="big">#1</p>
    <p class="tail">New Years resolution<br>set by Americans</p>
  </section>

  <section class="stat stat-keep">
    <p class="lead">However, only</p>
    <svg width="250" height="250" viewBox="0 0 250 250" aria-label="Pie chart: 8 percent">
      <circle cx="125" cy="125" r="125" fill="var(--navy)"/>
      <path d="M125 125 L125 0 A125 125 0 0 0 63.6 16.1 Z" fill="var(--green)"/>
      <text x="125" y="145" text-anchor="middle" font-family="Roboto Condensed, sans-serif" font-size="48" font-weight="700" fill="var(--green)">8%</text>
    </svg>
    <p class="tail">Keep those<br>resolutions</p>
  </section>

  <div class="count-badge">5</div>
  <h2 class="steps-band">Steps to setting and reaching your<br>weight loss resolution this year</h2>

  <div class="rail rail-left"></div>
  <div class="rail rail-right"></div>

  <article class="step" style="top:1311px">
    <span class="step-num">1</span>
    <div class="step-icon">
      <svg width="70" height="70" viewBox="0 0 70 70"><circle cx="35" cy="35" r="28" fill="none" stroke="#fff" stroke-width="6"/><circle cx="35" cy="35" r="8" fill="#fff"/></svg>
    </div>
    <div class="step-bar"></div>
    <h3 class="step-name">Reflect</h3>
    <p class="step-text">Get clear on why the achievement of your resolution is important. You'll need to come back to this if you falter!</p>
  </article>

  <article class="step" style="top:1490px">
    <span class="step-num">2</span>
    <div class="step-icon">
      <svg width="76" height="70" viewBox="0 0 76 70" fill="none" stroke="#fff" stroke-width="4" stroke-linecap="round">
        <path d="M4 12 l5 5 l9 -10"/><path d="M4 35 l5 5 l9 -10"/><path d="M4 58 l5 5 l9 -10"/>
        <path d="M28 12 H72"/><path d="M28 35 H72"/><path d="M28 58 H72"/>
      </svg>
    </div>
    <div class="step-bar"></div>
    <h3 class="step-name">Resolve</h3>
    <p class="step-text">Set a weight loss goal for the year that is realistic, then break this up into even shorter term goals of 30-60 days, with a specific diet and activity plan to guide you.</p>
  </article>

  <article class="step" style="top:1669px">
    <span class="step-num">3</span>
    <div class="step-icon">
      <svg width="70" height="70" viewBox="0 0 70 70" fill="none" stroke="#fff" stroke-width="6" stroke-linecap="round">
        <path d="M22 12 A27 27 0 1 0 48 12"/><path d="M10 8 H24 V22"/>
      </svg>
    </div>
    <div class="step-bar"></div>
    <h3 class="step-name">Replace</h3>
    <p class="step-text">Clear out your pantry and stock up with only healthy foods. Then work to build new activity and eating habits that take the place of your current habits.</p>
  </article>

  <article class="step" style="top:1849px">
    <span class="step-num">4</span>
    <div class="step-icon">
      <svg width="60" height="76" viewBox="0 0 60 76" fill="none" stroke="#fff" stroke-width="5" stroke-linecap="round">
        <rect x="20" y="4" width="20" height="40" rx="10" fill="#fff"/>
        <path d="M10 32 A20 20 0 0 0 50 32"/><path d="M30 52 V70"/><path d="M20 70 H40"/>
      </svg>
    </div>
    <div class="step-bar"></div>
    <h3 class="step-name">Record</h3>
    <p class="step-text">Track your progress daily, tell your family and friends about your resolution to create more accountability, and recruit a partner to share your journey.</p>
  </article>

  <article class="step" style="top:2023px">
    <span class="step-num">5</span>
    <div class="step-icon">
      <svg width="70" height="76" viewBox="0 0 70 76">
        <path d="M18 6 H52 V28 A17 17 0 0 1 18 28 Z" fill="#fff"/>
        <path d="M18 12 H6 V20 A12 12 0 0 0 18 32 M52 12 H64 V20 A12 12 0 0 1 52 32" fill="none" stroke="#fff" stroke-width="4"/>
        <rect x="31" y="44" width="8" height="14" fill="#fff"/><rect x="18" y="58" width="34" height="10" fill="#fff"/>
        <text x="35" y="30" text-anchor="middle" font-family="Roboto Condensed, sans-serif" font-size="18" font-weight="700" fill="var(--blue)">1</text>
      </svg>
    </div>
    <div class="step-bar"></div>
    <h3 class="step-name">Reward</h3>
    <p class="step-text">Set a weight loss goal for the year that is realistic, then break this up into even shorter term goals of 30-60 days, with a specific diet and activity plan to guide you.</p>
  </article>

  <div class="foot-rule"></div>
  <p class="site-url">www.SLIMBIRCH.com</p>

  <div class="brand-box">
    <span class="brand-dot"></span>
    <span class="brand-name">SlimBirch</span>
  </div>
</body>
</html>
```